Business cards for start-up accounting firm

I'm looking for a double sided business card ready for upload into Lumo print or similar print providers with no modification required by me.
I'm looking for something simple as i think cards that are too 'busy' actually detract from the message. I have some thoughts but more than happy to see what comes up. The logo i have came out of left field and i love it the moment i saw it!

My thoughts:

Side 1: Just the logo, perhaps on a dark grey or charcoal background to make the logo colours stand out?

Side 2: The call to action from me website 'Looking for a more relaxed, friendly and interactive relationship with your accountant?' with my contact information
Name: Gus Tarrow
Email: gus@ledgerowl.com.au
Website: www.ledgerowl.com.au
Phone: 1300 762 349

The call to action needs to be the first thing they see when they look at side 2. If it helps to know what we do and how we do it there is a draft website at www.ledgerowl.com.au

Like i said, happy to consider anything that comes up :)

Target Market(s)

i'm targeting small business owners who experience a lot of stress around finacial reporting and have had bad experiences with accountants in the past.

Industry/Entity Type

Accounting

Contact Information for Business Card

Contained in the Description

Font styles to use
Serif
Sans Serif
Other font styles liked:
• See logo files attached

Colors
474747

Requirements
Must have
• My logo, slogan and contact information

```html
<!DOCTYPE html>
<html lang="en">
<head>
<meta charset="utf-8">
<title>Ledger Owl – Business Cards</title>
<link rel="stylesheet" href="https://fonts.googleapis.com/css2?family=Open+Sans:wght@400;600;800&display=swap">
<style>
  :root {
    --backdrop: #5b3d2a;
    --card: #ffffff;
    --brand-purple: #7d2a6e;
    --ink: #1e1e1e;
    --rule: #3a3a3a;
  }
  * { box-sizing: border-box; margin: 0; padding: 0; }
  html, body { width: 1200px; height: 1000px; overflow: hidden; }
  body {
    position: relative;
    background: var(--backdrop);
    font-family: "Open Sans", Arial, sans-serif;
  }
  .card {
    position: absolute;
    left: 265px;
    width: 665px;
    height: 397px;
    background: var(--card);
    border-radius: 24px;
    box-shadow: 0 4px 12px rgba(0,0,0,0.35);
  }
  .card--info { top: 73px; }
  .card--brand { top: 532px; }

  .call-to-action {
    position: absolute;
    top: 127px;
    left: 0; right: 0;
    text-align: center;
    color: var(--brand-purple);
    font-weight: 600;
    font-size: 22px;
    line-height: 29px;
  }
  .holder-name {
    position: absolute;
    top: 273px;
    left: 0; right: 0;
    text-align: center;
    color: var(--ink);
    font-size: 17px;
    letter-spacing: 0.3px;
  }
  .divider {
    position: absolute;
    top: 316px;
    left: 40px;
    width: 585px;
    height: 2px;
    background: linear-gradient(90deg, rgba(58,58,58,0), var(--rule) 50%, rgba(58,58,58,0));
  }
  .contact-row {
    position: absolute;
    top: 336px;
    left: 40px;
    right: 38px;
    display: flex;
    justify-content: space-between;
    list-style: none;
    font-size: 15px;
    color: var(--ink);
  }
  .contact-row li { display: flex; align-items: center; gap: 7px; }
  .contact-row svg { width: 14px; height: 14px; fill: var(--brand-purple); }

  .brand-name {
    position: absolute;
    top: 156px;
    left: 0; right: 0;
    text-align: center;
    color: var(--brand-purple);
    font-weight: 800;
    font-size: 62px;
    line-height: 1;
    letter-spacing: 1px;
  }
</style>
</head>
<body>
  <section class="card card--info">
    <p class="call-to-action">Looking for a more relaxed, friendly and interactive<br>relationship with your accountant?</p>
    <p class="holder-name">GUS TARROW</p>
    <div class="divider"></div>
    <ul class="contact-row">
      <li>
        <svg viewBox="0 0 16 16" aria-hidden="true"><path d="M1 6c0-3 3-4 7-4s7 1 7 4v1h-4V5.5H5V7H1z M3 8h10l1 6H2z"/></svg>
        1300 762 349
      </li>
      <li>
        <svg viewBox="0 0 16 16" aria-hidden="true"><path d="M1 3h14v10H1z M2 4l6 5 6-5" stroke="#fff" stroke-width="1"/></svg>
        gus@ledgerowl.com.au
      </li>
      <li>
        <svg viewBox="0 0 16 16" aria-hidden="true"><circle cx="7" cy="7" r="6"/><path d="M9 9l6 3-3 1-1 3z" stroke="#fff" stroke-width="0.8"/></svg>
        www.ledgerowl.com.au
      </li>
    </ul>
  </section>

  <section class="card card--brand">
    <h1 class="brand-name">LEDGER OWL</h1>
  </section>
</body>
</html>
```